We have a new logo so we need to change our business card

We're super Happy with our current cards but I think with a new logo should come a new design. I wouldn't mind seeing the icons that we used on the back last time reused on this card. Please feel free to visit our website to get a sense for our brand www.brindlewick.ca

I need the final final to have contact info for:

Gordon Hasley
Co-Owner
info@brindlewick.ca
778-315-6207

and

Marjorie Hasley
Co-Owner
info@brindlewick.ca
778-342-5810

Target Market(s)

Female dog owners, 21 to 70

Industry/Entity Type

pet industry

Contact Information for Business Card

included in brief

Requirements
Should not have
• We do not want it to look cartonish

```html
<!DOCTYPE html>
<html lang="en">
<head>
<meta charset="utf-8">
<title>Brindlewick Business Card</title>
<link rel="stylesheet" href="https://fonts.googleapis.com/css2?family=Montserrat:wght@400;500;600;800&display=swap">
<style>
  :root {
    --backdrop: #bdbdbd;
    --leaf-green: #97cb60;
    --leaf-green-deep: #88b757;
    --ink: #1d1d1d;
    --paper: #ffffff;
    --mist: #e6e6e6;
    --card-shadow: 0 10px 24px rgba(0, 0, 0, 0.28);
  }
  * { box-sizing: border-box; margin: 0; padding: 0; }
  html, body {
    width: 1200px;
    height: 900px;
    overflow: hidden;
    background: var(--backdrop);
    font-family: "Montserrat", Arial, sans-serif;
  }
  .card {
    position: absolute;
    width: 560px;
    height: 320px;
    border-radius: 26px;
    overflow: hidden;
    box-shadow: var(--card-shadow);
  }
  .card--front { left: 80px; top: 90px; background: var(--leaf-green); }
  .card--back { left: 560px; top: 490px; background: var(--paper); }

  .brand-watermark {
    position: absolute;
    border-radius: 50%;
  }
  .card--front .brand-watermark {
    width: 300px; height: 300px; right: -40px; top: -10px;
    background: var(--leaf-green-deep);
  }
  .card--back .brand-watermark {
    width: 330px; height: 330px; right: -60px; top: -70px;
    background: var(--mist);
  }

  .wordmark {
    position: absolute;
    display: flex;
    align-items: center;
    gap: 14px;
  }
  .wordmark__dot {
    width: 62px; height: 62px; border-radius: 50%;
    flex: none;
  }
  .wordmark__name {
    font-weight: 800;
    font-size: 44px;
    letter-spacing: -0.5px;
    line-height: 1;
  }
  .card--front .wordmark { left: 110px; top: 128px; }
  .card--front .wordmark__dot { background: var(--paper); }
  .card--front .wordmark__name { color: var(--paper); }

  .card--back .wordmark { left: 40px; top: 52px; }
  .card--back .wordmark__dot { background: var(--leaf-green); }
  .card--back .wordmark__name { color: var(--ink); }

  .contact {
    position: absolute;
    left: 48px;
    top: 160px;
  }
  .contact__name {
    color: var(--leaf-green);
    font-weight: 600;
    font-size: 24px;
    letter-spacing: 0.5px;
    text-transform: uppercase;
  }
  .contact__role {
    color: var(--ink);
    font-size: 15px;
    margin-top: 2px;
  }
  .contact__list {
    list-style: none;
    margin-top: 14px;
  }
  .contact__item {
    display: flex;
    align-items: center;
    gap: 8px;
    color: var(--ink);
    font-size: 15px;
    line-height: 22px;
  }
  .contact__icon { width: 14px; height: 14px; flex: none; }

  .social {
    position: absolute;
    right: 34px;
    top: 150px;
    display: flex;
    gap: 8px;
  }
  .social__dot {
    width: 26px; height: 26px; border-radius: 50%;
    background: var(--leaf-green);
  }
</style>
</head>
<body>

<section class="card card--front" aria-label="Card front">
  <div class="brand-watermark" aria-hidden="true"></div>
  <div class="wordmark">
    <span class="wordmark__dot" aria-hidden="true"></span>
    <span class="wordmark__name">Brindlewick</span>
  </div>
</section>

<section class="card card--back" aria-label="Card back">
  <div class="brand-watermark" aria-hidden="true"></div>
  <div class="wordmark">
    <span class="wordmark__dot" aria-hidden="true"></span>
    <span class="wordmark__name">Brindlewick</span>
  </div>

  <div class="social" aria-label="Social profiles">
    <span class="social__dot"></span>
    <span class="social__dot"></span>
  </div>

  <div class="contact">
    <p class="contact__name">Gordon Hasley</p>
    <p class="contact__role">Co-Owner</p>
    <ul class="contact__list">
      <li class="contact__item">
        <svg class="contact__icon" viewBox="0 0 16 16" aria-hidden="true"><path d="M3 1.5l3 .5 1 3.5-2 1.2a9 9 0 0 0 4.3 4.3L10.5 9l3.5 1 .5 3-2 1.5C6.5 14.5 1.5 9.5 1.5 3.5z" fill="#97cb60"/></svg>
        778-315-6207
      </li>
      <li class="contact__item">
        <svg class="contact__icon" viewBox="0 0 16 16" aria-hidden="true"><rect x="1" y="3" width="14" height="10" fill="#97cb60"/><path d="M1 3l7 6 7-6" fill="none" stroke="#fff" stroke-width="1.3"/></svg>
        info@brindlewick.ca
      </li>
      <li class="contact__item">
        <svg class="contact__icon" viewBox="0 0 16 16" aria-hidden="true"><g fill="none" stroke="#97cb60" stroke-width="1.4"><circle cx="8" cy="8" r="6.5"/><ellipse cx="8" cy="8" rx="3" ry="6.5"/><path d="M1.5 8h13M2.5 5h11M2.5 11h11"/></g></svg>
        www.brindlewick.ca
      </li>
    </ul>
  </div>
</section>

</body>
</html>
```